Tallwater Marketing Business Card

Business card using new logo for marketing consulting company based in Silicon Valley. Limited information on card now (name, phone number, email, website), but room to add mailing address later.

```html
<!DOCTYPE html>
<html lang="en">
<head>
<meta charset="utf-8">
<title>Tallwater Marketing Business Card</title>
<link rel="stylesheet" href="https://fonts.googleapis.com/css2?family=Lato:wght@400&family=Open+Sans:wght@400&display=swap">
<style>
  :root {
    --sky: #48b9e7;
    --navy: #1f2d4f;
    --grey: #808080;
    --white: #ffffff;
  }
  * { margin: 0; padding: 0; box-sizing: border-box; }
  html, body { width: 1200px; height: 686px; overflow: hidden; background: var(--white); }
  .card {
    position: relative;
    width: 1200px;
    height: 686px;
    background: var(--white);
    overflow: hidden;
  }
  .brand-dot {
    position: absolute;
    left: 560px;
    top: 115px;
    width: 80px;
    height: 80px;
    border-radius: 50%;
    background: var(--sky);
  }
  .brand {
    position: absolute;
    left: 0;
    right: 0;
    top: 280px;
    text-align: center;
    font-family: "Open Sans", sans-serif;
    font-weight: 400;
    color: var(--sky);
  }
  .brand-name {
    font-size: 66px;
    line-height: 1;
    letter-spacing: 1px;
  }
  .brand-tagline {
    display: flex;
    align-items: center;
    justify-content: center;
    gap: 14px;
    margin-top: 12px;
    font-size: 26px;
    letter-spacing: 6px;
  }
  .brand-tagline::before,
  .brand-tagline::after {
    content: "";
    width: 76px;
    height: 2px;
    background: var(--grey);
  }
  .contact-band {
    position: absolute;
    left: 0;
    top: 497px;
    width: 1200px;
    height: 189px;
    background: var(--sky);
  }
  .contact-list {
    position: absolute;
    left: 0;
    top: 469px;
    width: 1200px;
    list-style: none;
  }
  .contact-item {
    position: absolute;
    top: 0;
    width: 292px;
    margin-left: -146px;
    text-align: center;
  }
  .contact-item:nth-child(1) { left: 163px; }
  .contact-item:nth-child(2) { left: 455px; }
  .contact-item:nth-child(3) { left: 746px; }
  .contact-item:nth-child(4) { left: 1038px; }
  .contact-icon {
    display: block;
    width: 55px;
    height: 55px;
    margin: 0 auto;
    background: var(--white);
    border: 2px solid var(--sky);
  }
  .contact-icon svg { display: block; width: 100%; height: 100%; }
  .contact-text {
    display: block;
    margin-top: 98px;
    transform: translateY(-50%);
    font-family: "Lato", sans-serif;
    font-size: 23px;
    color: var(--white);
    white-space: nowrap;
  }
</style>
</head>
<body>
  <main class="card">
    <div class="brand-dot"></div>
    <div class="brand">
      <div class="brand-name">TALLWATER</div>
      <div class="brand-tagline">MARKETING</div>
    </div>

    <div class="contact-band"></div>
    <ul class="contact-list">
      <li class="contact-item">
        <span class="contact-icon">
          <svg viewBox="0 0 55 55" aria-hidden="true">
            <circle cx="27.5" cy="21.5" r="5.5" fill="var(--sky)"/>
            <path d="M17 36 q0 -8 10.5 -8 q10.5 0 10.5 8 z" fill="var(--sky)"/>
          </svg>
        </span>
        <span class="contact-text">John Doe</span>
      </li>
      <li class="contact-item">
        <span class="contact-icon">
          <svg viewBox="0 0 55 55" aria-hidden="true">
            <path d="M21 18 l4 -1 l3 6 l-2.5 2 q2 4.5 6 6.5 l2 -2.5 l6 3 l-1 4 q-1.5 1.5 -4 1 q-9 -3 -13.5 -12.5 q-1 -3 0 -6.5 z" fill="var(--sky)"/>
          </svg>
        </span>
        <span class="contact-text">(123) 456 789 000</span>
      </li>
      <li class="contact-item">
        <span class="contact-icon">
          <svg viewBox="0 0 55 55" aria-hidden="true">
            <rect x="17" y="20" width="21" height="15" fill="var(--sky)"/>
            <path d="M17 20 l10.5 9 l10.5 -9" fill="none" stroke="var(--white)" stroke-width="1.6"/>
          </svg>
        </span>
        <span class="contact-text">contact@domain.com</span>
      </li>
      <li class="contact-item">
        <span class="contact-icon">
          <svg viewBox="0 0 55 55" aria-hidden="true">
            <circle cx="27.5" cy="27.5" r="10" fill="var(--sky)"/>
            <ellipse cx="27.5" cy="27.5" rx="4.5" ry="10" fill="none" stroke="var(--white)" stroke-width="1.4"/>
            <line x1="17.5" y1="27.5" x2="37.5" y2="27.5" stroke="var(--white)" stroke-width="1.4"/>
          </svg>
        </span>
        <span class="contact-text">www.website.com</span>
      </li>
    </ul>
  </main>
</body>
</html>
```